The Greenvale Open for Pitch Stars™

Please go to www.greenvaleopenstars.com and if you are a professional web designer you know what needs to be done!
I need a fresh, modern but still 'credible' design (authority!) - after all the event is an official World Championship!
Content (text, pics etc.) remains the same.
A new, trademarked logo has been developed and needs to be used throughout the site.
The site must include the possibility to be able to update/change content by ourselfs using a simple CMS.
Project duration: 5 days or less.
Main reason being for such a short period of time: we are AT PRESENT in negociations with all kinds of stakeholders and would like to impress them ASAP!
Could be an ongoing job for next couple of months.
Key words: official World Championship, golf, football, first sports cross over event ever, authority, fun, BRAZIL (hosting country), excitement, television, country's honour, another Global Trophy, PASSION!!
Pictures on website can be used - our/my responsibility.
Good luck!

Target Market(s)

(ex) Footballers - european soccer.
Golfers
People interested in sports

Industry/Entity Type

Event

Requirements
Must have
• Golf
Football
Brazil
Authority
World Championship

```html
<!DOCTYPE html>
<html lang="en">
<head>
<meta charset="utf-8">
<title>The Greenvale Open for Pitch Stars™</title>
<link rel="stylesheet" href="https://fonts.googleapis.com/css2?family=Oswald:wght@400;500&family=Ubuntu:wght@400;500&family=Roboto:wght@400;500;700&family=Parisienne&display=swap">
<style>
:root{
  --gold:#c9a94a;
  --gold-soft:#b39a4c;
  --gold-line:#a68b3a;
  --ink:#ffffff;
  --text:#e4e4e4;
  --muted:#9a9a9a;
  --page:#161616;
  --field:#a9a9a9;
  --field-text:#4c4c4c;
  --hero-top:#5d6550;
  --hero-mid:#7d8f48;
  --hero-low:#5c7a26;
}
*{box-sizing:border-box;margin:0;padding:0}
html,body{width:1168px;height:1200px;overflow:hidden;background:var(--page)}
body{position:relative;font-family:'Roboto',sans-serif;color:var(--text)}
.abs{position:absolute}

/* hero */
.hero{left:0;top:0;width:1168px;height:476px;overflow:hidden;border-top:4px solid var(--gold-line)}
.hero-photo{position:absolute;inset:0;background:linear-gradient(180deg,var(--hero-top) 0%,var(--hero-mid) 55%,var(--hero-low) 100%)}
.hero-shade{position:absolute;left:0;top:0;width:100%;height:95px;background:rgba(0,0,0,.35)}
.brand{left:100px;top:30px;display:flex;align-items:center;gap:10px}
.brand-dot{width:40px;height:40px;border-radius:50%;background:var(--gold)}
.brand-name{font-family:'Ubuntu',sans-serif;font-weight:500;font-size:13px;line-height:16px;color:var(--ink);width:160px}
.phone{left:898px;top:22px;display:flex;align-items:center;gap:6px;font-family:'Ubuntu',sans-serif;font-size:18px;color:var(--ink)}
.nav{left:685px;top:64px;display:flex;gap:24px;font-family:'Oswald',sans-serif;font-size:19px;text-transform:uppercase;letter-spacing:-.2px}
.nav a{color:var(--gold);text-decoration:none;text-shadow:0 1px 2px rgba(0,0,0,.6)}
.nav a.current{color:var(--ink)}
.quote{left:105px;font-family:'Parisienne',cursive;font-size:25px;line-height:35px;letter-spacing:.6px;word-spacing:4px;color:var(--ink);text-shadow:0 1px 3px rgba(0,0,0,.5)}
.dots{left:989px;top:455px;display:flex;gap:9px}
.dots span{width:10px;height:10px;background:#d8d8d8;border:1px solid #888}
.dots span.on{background:#fff}

/* quick contact */
.quick{left:0;top:476px;width:1168px;height:76px;background:linear-gradient(180deg,#3a3a3a,#1c1c1c);border-bottom:1px solid #444}
.quick-title{left:104px;top:7px;font-family:'Oswald',sans-serif;font-size:25px;line-height:30px;color:#e0e0e0}
.field{top:23px;height:33px;background:var(--field);border:1px solid #8a8a8a;font-family:'Ubuntu',sans-serif;font-size:14px;color:var(--field-text);padding:7px 10px}
.submit{left:955px;top:21px;width:99px;height:36px;background:var(--gold-line);border:1px solid #c3a956;font-family:'Ubuntu',sans-serif;font-size:20px;color:#fff;text-align:center;line-height:34px}

/* content */
.content{left:0;top:553px;width:1168px;height:647px;background:radial-gradient(ellipse at 50% 20%,#2a2a2a,#121212 70%)}
.section-title{font-family:'Ubuntu',sans-serif;font-size:23px;color:var(--gold)}
.rule{height:1px;background:#3a3a3a}
.intro-date{left:113px;top:70px;font-size:13px;font-weight:500;color:var(--ink)}
.intro p{font-size:13px;line-height:19.3px;color:var(--text);width:600px;text-align:justify;margin-bottom:16px}
.news-date{font-size:13px;font-weight:700;color:var(--ink);display:flex;align-items:center;gap:8px}
.news-head{font-size:13px;font-weight:700;color:var(--ink);margin-top:3px}
.news-body{font-size:13px;line-height:19.3px;color:var(--text);width:290px}
.read-more{font-size:13px;font-weight:500;color:var(--gold);margin-top:9px}
.player{width:140px;text-align:center}
.portrait{width:128px;height:128px;border-radius:50%;margin:0 auto;border:4px solid #5a5a5a;box-shadow:0 0 0 1px #222,0 4px 10px rgba(0,0,0,.6)}
.player-name{margin-top:14px;font-size:13px;font-weight:700;color:var(--ink)}
.player-country{font-size:13px;font-weight:500;color:var(--gold-soft);margin-top:2px}
.arrow{width:36px;height:36px}

/* footer */
.footer-links{left:114px;top:568px;display:flex;gap:20px;font-family:'Oswald',sans-serif;font-size:19px;color:#888;text-transform:uppercase}
.newsletter{left:566px;top:568px;font-family:'Oswald',sans-serif;font-size:19px;color:#666;text-transform:uppercase}
.email-in{left:568px;top:600px;width:187px;height:26px;background:#f2f2f2;font-size:14px;color:#777;padding:4px 9px;font-family:'Ubuntu',sans-serif}
.go{left:755px;top:600px;width:29px;height:26px;background:var(--gold-line);border:2px solid #e8e8e8;color:#fff;font-size:11px;font-weight:700;text-align:center;line-height:22px}
.copy{left:115px;top:615px;font-size:13px;color:#888}
.foot-brand{left:887px;top:558px;display:flex;align-items:center;gap:8px}
.social{top:609px;display:flex;gap:11px;left:888px}
.social span{width:26px;height:26px;border-radius:50%;background:#555;border:1px solid #777}
</style>
</head>
<body>

<header class="hero abs">
  <div class="hero-photo" role="img" aria-label="Hero photo: gloved hand placing a golf ball on a tee beside an iron club on a fairway"></div>
  <div class="hero-shade"></div>
  <div class="brand abs"><span class="brand-dot"></span><span class="brand-name">The Greenvale Open for Pitch Stars™</span></div>
  <div class="phone abs">
    <svg width="20" height="22" viewBox="0 0 20 22"><path d="M4 2c2-1 3 0 4 2l1 3c0 1-1 2-2 3 1 3 3 5 6 6 1-1 2-2 3-2l3 1c2 1 1 3 0 4-2 3-6 3-10-1S1 5 4 2z" fill="#fff"/></svg>
    <span>+ 34 611 482 903</span>
  </div>
  <nav class="nav abs">
    <a class="current">Home</a><a>Event</a><a>Ambassadors</a><a>GVO/Contact</a>
  </nav>
  <p class="quote abs" style="top:114px;width:375px">‘Championship is not about money but about countries honour.....!!’</p>
  <p class="quote abs" style="top:203px;width:318px">‘Event appeals to a huge audience: 80 million golfers and 300 million footballers world wide.’</p>
  <div class="dots abs"><span></span><span></span><span class="on"></span><span class="on"></span></div>
</header>

<section class="quick abs">
  <div class="quick-title abs">QUICK<br>CONTACT</div>
  <div class="field abs" style="left:220px;width:147px">Name</div>
  <div class="field abs" style="left:378px;width:186px">Email</div>
  <div class="field abs" style="left:576px;width:137px">Subject</div>
  <div class="field abs" style="left:726px;width:217px">Message</div>
  <div class="submit abs">SUBMIT</div>
</section>

<main class="content abs">
  <div class="abs" style="left:113px;top:24px;display:flex;align-items:center;gap:10px">
    <span style="width:26px;height:26px;border-radius:50%;background:var(--gold)"></span>
    <h1 class="section-title" style="font-weight:400">The Greenvale Open For Pitch Stars ©</h1>
  </div>
  <div class="rule abs" style="left:113px;top:60px;width:600px"></div>
  <div class="intro-date abs">June 5-8, 2014, Rio de Janeiro, Brazil</div>
  <div class="intro abs" style="left:114px;top:97px">
    <p>One doesn’t need to be a fanatical supporter of either golf or football to get a sense of just how much interest and excitement the Greenvale Open for Pitch Stars© will generate: an A-list of current and former players and coaches from the world’s most popular spectator sport, playing the world’s fastest growing participation sport, on the world’s most beautiful golf courses, just has to be a winner!</p>
    <p>"These guys have performed in front of millions of people on a weekly basis. It will be fascinating to see how they hold their nerves outside their comfort zones but still in a very competitive environment…"</p>
  </div>

  <div class="abs" style="left:772px;top:24px;display:flex;align-items:center;gap:8px">
    <svg width="17" height="17" viewBox="0 0 17 17"><rect width="17" height="17" rx="3" fill="#666"/><circle cx="4.5" cy="12.5" r="1.8" fill="#222"/><path d="M3 7a7 7 0 0 1 7 7M3 3a11 11 0 0 1 11 11" stroke="#222" stroke-width="2" fill="none"/></svg>
    <h2 class="section-title" style="font-weight:400">Latest News</h2>
  </div>
  <div class="rule abs" style="left:772px;top:60px;width:290px"></div>
  <div class="abs" style="left:772px;top:68px">
    <div class="news-date"><svg width="17" height="16" viewBox="0 0 17 16"><rect x="1" y="2" width="15" height="13" fill="#666"/><rect x="1" y="2" width="15" height="3" fill="#888"/><g fill="#333"><rect x="3" y="7" width="2" height="2"/><rect x="7" y="7" width="2" height="2"/><rect x="11" y="7" width="2" height="2"/><rect x="3" y="11" width="2" height="2"/><rect x="7" y="11" width="2" height="2"/></g></svg>October 25 , 2013</div>
    <div class="news-head">President RGF: 'Event vitally important'</div>
    <p class="news-body">A delegation of GVO Marketing is at present in Rio de Janeiro, Brazil, for the purpose of selecting the most challenging golf course to host the inaugural Greenvale Open for Pitch Stars™ in June 2014.</p>
    <div class="read-more">Read More ▸</div>
  </div>

  <div class="rule abs" style="left:113px;top:247px;width:950px"></div>
  <h2 class="section-title abs" style="left:113px;top:262px;font-weight:400">Our Potential Candidates</h2>
  <div class="rule abs" style="left:113px;top:296px;width:268px;background:#555"></div>

  <svg class="arrow abs" style="left:114px;top:365px" viewBox="0 0 36 36"><circle cx="18" cy="18" r="17" fill="#6a6a6a" stroke="#999"/><path d="M21 11l-8 7 8 7z" fill="#2a2a2a"/></svg>
  <svg class="arrow abs" style="left:1018px;top:365px" viewBox="0 0 36 36"><circle cx="18" cy="18" r="17" fill="#6a6a6a" stroke="#999"/><path d="M15 11l8 7-8 7z" fill="#2a2a2a"/></svg>

  <div class="player abs" style="left:164px;top:319px"><div class="portrait" role="img" aria-label="Photo of candidate Marlow swinging a golf club" style="background:linear-gradient(180deg,#4f6a55,#2f6f9f)"></div><div class="player-name">Marlow</div><div class="player-country">(England)</div></div>
  <div class="player abs" style="left:332px;top:319px"><div class="portrait" role="img" aria-label="Photo of candidate Vermeer on a golf course" style="background:linear-gradient(180deg,#7f9ab0,#2a3550)"></div><div class="player-name">Vermeer</div><div class="player-country">(Holland)</div></div>
  <div class="player abs" style="left:505px;top:319px"><div class="portrait" role="img" aria-label="Photo of candidate Ashcombe following through a golf swing" style="background:linear-gradient(180deg,#6a7260,#4a3a3a)"></div><div class="player-name">Ashcombe</div><div class="player-country">(England)</div></div>
  <div class="player abs" style="left:686px;top:319px"><div class="portrait" role="img" aria-label="Photo of candidate Serrano putting on a green" style="background:linear-gradient(180deg,#5a7045,#8a8a6a)"></div><div class="player-name">Serrano</div><div class="player-country">(Spain)</div></div>
  <div class="player abs" style="left:864px;top:319px"><div class="portrait" role="img" aria-label="Photo of candidate Van Dalen in a navy polo shirt" style="background:linear-gradient(180deg,#8a8a88,#1f2a44)"></div><div class="player-name">Van Dalen</div><div class="player-country">(Holland)</div></div>

  <div class="rule abs" style="left:113px;top:539px;width:950px"></div>

  <nav class="footer-links abs"><span>Home</span><span>Event</span><span>Ambassadors</span><span>GVO/Contact</span></nav>
  <div class="newsletter abs">Newsletter Signup</div>
  <div class="email-in abs">Enter your e-mail address</div>
  <div class="go abs">GO</div>
  <div class="copy abs">© 2013 greenvaleopenstars.&nbsp; |&nbsp; All Rights Reserved</div>
  <div class="foot-brand abs"><span style="width:24px;height:24px;border-radius:50%;background:var(--gold)"></span><span class="brand-name" style="width:120px;font-size:11px;line-height:13px">The Greenvale Open for Pitch Stars™</span></div>
  <div class="social abs"><span></span><span></span><span></span></div>
</main>

</body>
</html>
```